varo institute
Professional
Kemalettin Yurdak
Principal
Elementary School
48 Maple Rd.Scarborough,ON. M1K3P9
Tel:416-5521963 Fax:416-5521964
High School
217 Bellwood Road.Toronto, ON. M9M4R2
Tel:416-3760294 Fax:416-3760287
k.yurdak@varoinstitute.com
www.varoinstitute.com

```html
<!DOCTYPE html>
<html lang="en">
<head>
<meta charset="utf-8">
<title>varo institute stationery</title>
<link href="https://fonts.googleapis.com/css2?family=Open+Sans:wght@400;600;700&display=swap" rel="stylesheet">
<style>
  :root {
    --board: #3b3b3d;
    --paper: #ffffff;
    --navy: #233f73;
    --blue: #2f86c4;
    --orange: #e4553b;
    --ink: #3a3a3a;
    --faint: #eef3f8;
    --fold: #e4e4e4;
  }
  * { margin: 0; padding: 0; box-sizing: border-box; }
  html, body { width: 1200px; height: 684px; overflow: hidden; }
  body {
    background: var(--board);
    font-family: "Open Sans", Arial, sans-serif;
    color: var(--ink);
    position: relative;
  }
  .sheet {
    position: absolute;
    background: var(--paper);
    box-shadow: 0 3px 10px rgba(0,0,0,.45);
    overflow: hidden;
  }
  .brand {
    display: flex; align-items: center; gap: 5px;
    color: var(--navy); font-weight: 700; letter-spacing: .4px;
    white-space: nowrap;
  }
  .brand-dot { border-radius: 50%; background: var(--orange); flex: none; }

  /* letterhead */
  .letterhead { left: 182px; top: 29px; width: 418px; height: 626px; }
  .letterhead .brand { position: absolute; left: 50%; top: 62px; transform: translateX(-50%); font-size: 14px; }
  .letterhead .brand-dot { width: 15px; height: 15px; }
  .watermark { position: absolute; left: 124px; top: 236px; width: 170px; height: 170px; }
  .footer-band { position: absolute; left: 0; right: 0; }
  .letterhead .footer-band { top: 586px; }
  .footer-band .rule { height: 2px; background: var(--orange); }
  .footer-band .band {
    background: var(--blue); color: #fff; text-align: center;
    font-size: 5.5px; line-height: 8px; padding: 3px 0;
  }
  .footer-band .web { text-align: center; font-size: 5.5px; color: var(--ink); padding-top: 4px; }

  /* business cards */
  .card { left: 65px; width: 192px; }
  .card-front { top: 245px; height: 110px; }
  .card-front .brand { position: absolute; left: 26px; top: 40px; font-size: 12px; }
  .card-front .brand-dot { width: 13px; height: 13px; }
  .card-front .web { position: absolute; left: 26px; top: 92px; font-size: 5px; }
  .card-back { top: 365px; height: 106px; }
  .card-back .brand { position: absolute; left: 26px; top: 10px; font-size: 12px; }
  .card-back .brand-dot { width: 13px; height: 13px; }
  .card-back .name-band {
    position: absolute; left: 0; right: 0; top: 34px;
    background: var(--blue); color: #fff; text-align: center;
    font-size: 5.5px; line-height: 10px;
  }
  .card-back .name-band b { font-weight: 700; }
  .card-back .contact {
    position: absolute; left: 0; right: 0; top: 49px;
    text-align: center; font-size: 4.4px; line-height: 6.2px;
  }
  .card-back .contact strong { color: var(--navy); }

  /* envelopes */
  .envelope { left: 643px; width: 490px; }
  .envelope-back { top: 96px; height: 199px; }
  .envelope-back .flap { position: absolute; inset: 0; }
  .envelope-back .brand { position: absolute; left: 50%; top: 46px; transform: translateX(-50%); font-size: 11px; }
  .envelope-back .brand-dot { width: 12px; height: 12px; }
  .envelope-front { top: 367px; height: 226px; }
  .envelope-front .brand { position: absolute; left: 50%; top: 44px; transform: translateX(-50%); font-size: 12px; }
  .envelope-front .brand-dot { width: 13px; height: 13px; }
  .envelope-front .footer-band { top: 188px; }
</style>
</head>
<body>

<section class="sheet letterhead">
  <div class="brand"><span class="brand-dot"></span>VARO INSTITUTE</div>
  <svg class="watermark" viewBox="0 0 170 170" aria-hidden="true">
    <circle cx="85" cy="85" r="78" fill="none" stroke="var(--faint)" stroke-width="10"/>
  </svg>
  <div class="footer-band">
    <div class="rule"></div>
    <div class="band">
      <b>Elementary School</b> 48 Maple Rd.Scarborough,ON. M1K3P9 | Tel:416-5521963 Fax:416-5521964<br>
      <b>High School</b> 217 Bellwood Road.Toronto, ON. M9M4R2 | Tel:416-3760294 Fax:416-3760287
    </div>
    <div class="web">k.yurdak@varoinstitute.com | www.varoinstitute.com</div>
  </div>
</section>

<section class="sheet card card-front">
  <div class="brand"><span class="brand-dot"></span>VARO INSTITUTE</div>
  <div class="web">www.varoinstitute.com</div>
</section>

<section class="sheet card card-back">
  <div class="brand"><span class="brand-dot"></span>VARO INSTITUTE</div>
  <div class="name-band"><b>Kemalettin Yurdak</b> | Principal</div>
  <div class="contact">
    <strong>Elementary School</strong><br>
    48 Maple Rd.Scarborough,ON. M1K3P9<br>
    Tel:416-5521963 Fax:416-5521964<br>
    <strong>High School</strong><br>
    217 Bellwood Road.Toronto, ON. M9M4R2<br>
    Tel:416-3760294 Fax:416-3760287<br>
    k.yurdak@varoinstitute.com
  </div>
</section>

<section class="sheet envelope envelope-back">
  <svg class="flap" viewBox="0 0 490 199" preserveAspectRatio="none" aria-hidden="true">
    <path d="M0 0 L245 115 L490 0" fill="none" stroke="var(--fold)" stroke-width="1.5"/>
    <path d="M0 199 L195 92 M490 199 L295 92" fill="none" stroke="#efefef" stroke-width="1"/>
  </svg>
  <div class="brand"><span class="brand-dot"></span>VARO INSTITUTE</div>
</section>

<section class="sheet envelope envelope-front">
  <div class="brand"><span class="brand-dot"></span>VARO INSTITUTE</div>
  <div class="footer-band">
    <div class="rule"></div>
    <div class="band">
      <b>Elementary School</b> 48 Maple Rd.Scarborough,ON. M1K3P9 | <b>High School</b> 217 Bellwood Road.Toronto, ON. M9M4R2<br>
      Tel:416-5521963 Fax:416-5521964 | Tel:416-3760294 Fax:416-3760287 | k.yurdak@varoinstitute.com | www.varoinstitute.com
    </div>
  </div>
</section>

</body>
</html>
```